BRCW Business Cards

Business Cards should contain:
Bright Ridgeway Coating Works
Colin Pardew
M: 0418 675 913
E: brightRCW@tealmail.example
BRCW logo
TCG logo
Painting & Decorating
Licence # 671392K
slogan: feel the mark of modern perfection

Target Market(s)

all aspect of painting

Industry/Entity Type

Trade

Contact Information for Business Card

Colin Pardew
M: 0418 675 913
E: brightRCW@tealmail.example
BRCW logo
TCG logo
Painting & Decorating
Licence # 671392K

Font styles to use
Serif
Sans Serif

Requirements
Must have
• clear design with nice backround
• two sides
• smal TCG logo
Nice to have
• easy to read
Should not have
• mess
• black
• plastics form

```html
<!DOCTYPE html>
<html lang="en">
<head>
<meta charset="utf-8">
<title>BRCW Business Cards</title>
<link rel="stylesheet" href="https://fonts.googleapis.com/css2?family=Alegreya:wght@500;600&family=Lato:wght@400&display=swap">
<style>
  :root {
    --page: #f4f5f7;
    --card: #ffffff;
    --accent: #f05a28;
    --ink: #1f4a47;
    --brand: #174b45;
    --badge: #2a57a6;
    --disc: #dce6e3;
    --disc-ring: #e8efed;
    --swatch-deep: #2a4f9a;
    --swatch-mid: #1f84b8;
    --swatch-light: #21b6c9;
  }
  * { margin: 0; padding: 0; box-sizing: border-box; }
  html, body { width: 1200px; height: 1023px; overflow: hidden; background: var(--page); }
  .canvas { position: relative; width: 1200px; height: 1023px; }
  .card { position: absolute; width: 547px; height: 312px; }
  .card-front { left: 116px; top: 141px; background: var(--card); }
  .card-back { left: 511px; top: 536px; overflow: hidden; }

  .company {
    position: absolute; left: 38px; top: 64px;
    font-family: "Alegreya", Georgia, serif; font-weight: 600;
    font-size: 23px; line-height: 26px; color: var(--accent);
  }
  .service, .details {
    font-family: "Lato", Arial, sans-serif; font-weight: 400;
    color: var(--ink); font-size: 15px;
  }
  .service { position: absolute; left: 38px; top: 132px; }
  .person {
    position: absolute; left: 38px; top: 170px;
    font-family: "Alegreya", Georgia, serif; font-weight: 600;
    font-size: 22px; color: var(--accent);
  }
  .details { position: absolute; left: 38px; top: 199px; line-height: 18px; }
  .details .licence { margin-bottom: 7px; }

  .brand-mark {
    display: flex; align-items: center; gap: 10px;
    font-family: "Alegreya", Georgia, serif; font-weight: 600; color: var(--brand);
  }
  .brand-mark .dot { border-radius: 50%; background: var(--brand); flex: none; }
  .front-brand { position: absolute; left: 372px; top: 60px; font-size: 32px; }
  .front-brand .dot { width: 22px; height: 22px; }
  .partner-badge {
    position: absolute; left: 418px; top: 170px;
    width: 64px; height: 64px; border-radius: 50%; background: var(--badge);
  }

  .swatch-field {
    position: absolute; inset: 0;
    background: linear-gradient(110deg, var(--swatch-deep) 0%, var(--swatch-mid) 45%, var(--swatch-light) 100%);
  }
  .back-disc {
    position: absolute; left: 138px; top: 21px; width: 270px; height: 270px;
    border-radius: 50%; background: var(--disc); border: 7px solid var(--disc-ring);
    display: flex; align-items: center; justify-content: center;
  }
  .back-brand { font-size: 44px; }
  .back-brand .dot { width: 30px; height: 30px; }
</style>
</head>
<body>
<main class="canvas">
  <section class="card card-front">
    <h1 class="company">Bright Ridgeway<br>Coating Works</h1>
    <p class="service">Painting &amp; Decorating</p>
    <h2 class="person">Colin Pardew</h2>
    <div class="details">
      <p class="licence">Licence # 671392K</p>
      <p>0418 675 913</p>
      <p>brightRCW@tealmail.example</p>
    </div>
    <div class="brand-mark front-brand"><span class="dot"></span>BRCW</div>
    <div class="partner-badge" role="img" aria-label="TCG association badge"></div>
  </section>

  <section class="card card-back">
    <div class="swatch-field" role="img" aria-label="Blue and teal paint colour swatch grid"></div>
    <div class="back-disc">
      <div class="brand-mark back-brand"><span class="dot"></span>BRCW</div>
    </div>
  </section>
</main>
</body>
</html>
```